Harbor Networks Pty Ltd

We are a Sydney based IT services company, providing managed services for corporate clients, established for over 10 years. Amongst our services we provide full infrastructure support, maintenance and upgrades. We also provide helpdesk/remote support and cloud services.

We were hoping to keep our original colours and our logo (Blue and Green, please visit our website www.harbornetworks-demo.com.au) however we are looking for a new business card design (with better resolution and finish) with multiple variation of the blue and green colour design options. Happy for alternative suggestion. ie new blue and green / grey and green / blue and grey et and please feel free to update current logo size ie large or smaller. (Attached our current logo and business card desig)

Business

Contact Information for Business Card

Name, Title, Address, Contract Information, Company Name and Logo.
(QR code if possible)

Colors
0455a3
33a6d7
3276b5
85acd3
85cae6
9bcb3c
add136
cadf82
e9f1ce

```html
<!DOCTYPE html>
<html lang="en">
<head>
<meta charset="utf-8">
<title>Harbor Networks – Business Card</title>
<link href="https://fonts.googleapis.com/css2?family=Source+Sans+3:wght@400;600&display=swap" rel="stylesheet">
<style>
  :root {
    --backdrop: #e4e4e2;
    --card-dark: #1b1b1b;
    --card-light: #ffffff;
    --brand-blue: #3276b5;
    --ink: #1e1e1e;
    --ink-light: #f2f2f2;
  }
  * { box-sizing: border-box; margin: 0; padding: 0; }
  html, body {
    width: 1200px; height: 1000px; overflow: hidden;
    background: var(--backdrop);
    font-family: "Source Sans 3", "Open Sans", sans-serif;
  }
  .canvas { position: relative; width: 1200px; height: 1000px; }

  .card {
    position: absolute; width: 720px; height: 430px;
    box-shadow: 0 6px 18px rgba(0,0,0,0.25);
  }
  .card--front { left: 200px; top: 40px; background: var(--card-dark); }
  .card--back  { left: 280px; top: 520px; background: var(--card-light); }

  /* Front */
  .front-text { position: absolute; right: 46px; top: 238px; text-align: right; }
  .front-tagline {
    color: var(--brand-blue); font-size: 38px; font-weight: 400;
    letter-spacing: 1px; line-height: 1;
  }
  .front-web {
    color: var(--ink-light); font-size: 21px; letter-spacing: 2px;
    margin-top: 8px;
  }

  /* Back */
  .brand {
    position: absolute; right: 40px; top: 36px;
    display: flex; align-items: center; gap: 12px;
  }
  .brand-square { width: 22px; height: 22px; background: var(--brand-blue); }
  .brand-name { color: var(--ink); font-size: 40px; font-weight: 400; line-height: 1; }

  .holder { position: absolute; left: 56px; top: 220px; }
  .holder-name { color: var(--brand-blue); font-size: 27px; font-weight: 400; letter-spacing: 0.5px; line-height: 1.1; }
  .holder-title { color: var(--ink); font-size: 18px; }

  .contacts {
    position: absolute; right: 40px; top: 104px; text-align: right;
    color: var(--ink); font-size: 16px; line-height: 21px; list-style: none;
  }
  .contacts li { display: flex; justify-content: flex-end; align-items: center; gap: 7px; }
  .contacts svg { width: 14px; height: 14px; fill: var(--brand-blue); flex: none; }
  .contacts .plain { padding-right: 21px; }
  .contacts .gap { margin-top: 14px; }

  .company { position: absolute; right: 61px; top: 300px; text-align: right; font-size: 17px; line-height: 21px; color: var(--ink); }
  .company-name { color: var(--brand-blue); letter-spacing: 0.5px; }
</style>
</head>
<body>
<main class="canvas">

  <section class="card card--front" aria-label="Card front">
    <div class="front-text">
      <p class="front-tagline">MANAGED IT SERVICES</p>
      <p class="front-web">www.harbornetworks-demo.com.au</p>
    </div>
  </section>

  <section class="card card--back" aria-label="Card back">
    <div class="brand">
      <span class="brand-square"></span>
      <span class="brand-name">harbor networks</span>
    </div>

    <ul class="contacts">
      <li>1300 555 010
        <svg viewBox="0 0 16 16"><path d="M3.5 1l3 3-1.6 1.8c.8 2 2.3 3.5 4.3 4.3L11 8.5l3 3-1.7 2.7C7 14 2 9 1.8 3.7z"/></svg></li>
      <li>+61 2 5550 1234
        <svg viewBox="0 0 16 16"><path d="M3.5 1l3 3-1.6 1.8c.8 2 2.3 3.5 4.3 4.3L11 8.5l3 3-1.7 2.7C7 14 2 9 1.8 3.7z"/></svg></li>
      <li>+61 400 555 123
        <svg viewBox="0 0 16 16"><path d="M4 1h8v14H4zM5.5 2.5v9h5v-9z"/></svg></li>
      <li>+61 2 5550 9876
        <svg viewBox="0 0 16 16"><path d="M4 1h8v4H4zM1 6h14v6h-3v3H4v-3H1zM5.5 10v3.5h5V10z"/></svg></li>
      <li>support@harbornetworks-demo.com.au
        <svg viewBox="0 0 16 16"><path d="M1 3h14v10H1zM2.5 4.5L8 9l5.5-4.5z"/></svg></li>
      <li>dana.morrow@harbornetworks-demo.com.au
        <svg viewBox="0 0 16 16"><path d="M1 3h14v10H1zM2.5 4.5L8 9l5.5-4.5z"/></svg></li>
    </ul>

    <div class="holder">
      <p class="holder-name">DANA MORROW</p>
      <p class="holder-title">Director</p>
    </div>

    <address class="company" style="font-style: normal;">
      <p class="company-name">HARBOR NETWORKS PTY LTD</p>
      <p>Level 4, 18 Example Street,</p>
      <p>Sydney, NSW 2000, Australia</p>
    </address>
  </section>

</main>
</body>
</html>
```